Innovative Healthcare Technology Company needs a Business Card Design

We are in need of an innovative business card design for a new healthcare software company called "Brightwell Harbor Systems". We develop software that creates medical assessment applications and mobile e-learning prevention services to reduce risk behaviors in adolescent and young adults. Our initial product, the "MERIDIAN App", conducts a tailored sexual risk assessment and provides a doctor with an insightful patient report to improve sexual risk counseling and ultimately reduce unintended pregnancy, STDs, etc.

We would like the design to incorporate our logo and branding colors (attached) in an innovative and creative manner. The final design should communicate professionalism and healthcare innovation. Our tag line is "prevention is the solution" (doesn't necessarily need to be included) and our target audience is doctors, medical directors, and medical business administrators. Please visit our website for additional info ourlantrixhub.com. Be creative and we look forward to seeing your designs!

Target Market(s)

healthcare - doctors, medical directors and medical business administrators

Industry/Entity Type

Healthcare

Contact Information for Business Card

We would like the design to incorporate our logo and branding colors (attached) in an innovative and creative manner. The final design should communicate professionalism and healthcare innovation. Our tag line is "prevention is the solution" (doesn't necessarily need to be included)

Font styles to use
Other font styles liked:
• quicksand

Requirements
Must have
• our logo and brand colors
• Name, (Joan Ferraventi, PhD)
• Email (drjoan@ourlantrixhub.com)
• phone (555.213.8870)
• Website (ourlantrixhub.com)
Should not have
• cartoon look

```html
<!DOCTYPE html>
<html lang="en">
<head>
<meta charset="utf-8">
<title>Brightwell Harbor Systems — Business Card</title>
<link href="https://fonts.googleapis.com/css2?family=Quicksand:wght@400;500;600;700&display=swap" rel="stylesheet">
<style>
  :root {
    --backdrop: #d9dcdf;
    --card: #eef1f3;
    --card-edge: #d2d7dc;
    --navy: #1d3a6b;
    --green: #2f6d58;
    --ink: #2a3546;
  }
  * { margin: 0; padding: 0; box-sizing: border-box; }
  html, body {
    width: 1200px;
    height: 969px;
    overflow: hidden;
    background: var(--backdrop);
    font-family: "Quicksand", sans-serif;
  }
  .card {
    position: absolute;
    left: 80px;
    top: 187px;
    width: 1040px;
    height: 594px;
    background: var(--card);
    border: 1px solid var(--card-edge);
    border-radius: 22px;
    box-shadow: 0 14px 40px rgba(40, 50, 60, 0.18);
    overflow: hidden;
  }
  .company {
    position: absolute;
    left: 80px;
    top: 112px;
    display: flex;
    align-items: center;
    gap: 18px;
  }
  .company-name {
    font-size: 50px;
    font-weight: 500;
    line-height: 1.1;
    color: var(--navy);
    letter-spacing: 0.5px;
    white-space: nowrap;
  }
  .company-square {
    width: 28px;
    height: 28px;
    background: var(--navy);
    border-radius: 4px;
  }
  .edge-tab {
    position: absolute;
    left: 0;
    top: 292px;
    width: 20px;
    height: 82px;
    background: var(--navy);
    border-radius: 0 6px 6px 0;
  }
  .person-name {
    position: absolute;
    left: 80px;
    top: 290px;
    font-size: 33px;
    font-weight: 700;
    color: var(--navy);
  }
  .person-name .credential { font-size: 24px; font-weight: 700; }
  .person-title {
    position: absolute;
    left: 80px;
    top: 338px;
    font-size: 28px;
    font-weight: 400;
    color: var(--green);
  }
  .contact-list {
    position: absolute;
    left: 82px;
    top: 400px;
    list-style: none;
  }
  .contact-item {
    display: flex;
    align-items: center;
    height: 40px;
    font-size: 24px;
    font-weight: 500;
    color: var(--ink);
  }
  .contact-icon {
    width: 24px;
    height: 24px;
    margin-right: 14px;
    fill: var(--ink);
  }
</style>
</head>
<body>
  <div class="card">
    <div class="company">
      <div class="company-square"></div>
      <div class="company-name">Brightwell Harbor Systems</div>
    </div>

    <div class="edge-tab"></div>

    <div class="person-name">Joan Ferraventi, <span class="credential">PhD</span></div>
    <div class="person-title">CEO/Founder</div>

    <ul class="contact-list">
      <li class="contact-item">
        <svg class="contact-icon" viewBox="0 0 24 24" aria-hidden="true">
          <path d="M6.6 10.8c1.4 2.8 3.8 5.1 6.6 6.6l2.2-2.2c.3-.3.7-.4 1-.2 1.1.4 2.3.6 3.6.6.6 0 1 .4 1 1V20c0 .6-.4 1-1 1C10.6 21 3 13.4 3 4c0-.6.4-1 1-1h3.5c.6 0 1 .4 1 1 0 1.3.2 2.5.6 3.6.1.3 0 .7-.2 1L6.6 10.8z"/>
        </svg>
        555.213.8870
      </li>
      <li class="contact-item">
        <svg class="contact-icon" viewBox="0 0 24 24" aria-hidden="true">
          <path d="M3 5h18c.6 0 1 .4 1 1v12c0 .6-.4 1-1 1H3c-.6 0-1-.4-1-1V6c0-.6.4-1 1-1zm1 2.2V17h16V7.2l-8 5.3-8-5.3zM5.6 7 12 11.2 18.4 7H5.6z"/>
        </svg>
        drjoan@ourlantrixhub.com
      </li>
      <li class="contact-item">
        <svg class="contact-icon" viewBox="0 0 24 24" aria-hidden="true">
          <path d="M12 2a10 10 0 1 0 0 20 10 10 0 0 0 0-20zm-1 17.9A8 8 0 0 1 4.1 11H7c0 3.3 1.5 6.4 4 8.9zM7 9H4.3A8 8 0 0 1 11 4.1C9 6 7.6 7.4 7 9zm6 10.9c2.5-2.5 4-5.6 4-8.9h2.9a8 8 0 0 1-6.9 8.9zM17 9c-.6-1.6-2-3-4-4.9A8 8 0 0 1 19.7 9H17zm-8 2h6c0 2.6-1.1 5-3 7-1.9-2-3-4.4-3-7zm.3-2c.5-1.4 1.4-2.7 2.7-4 1.3 1.3 2.2 2.6 2.7 4H9.3z"/>
        </svg>
        ourlantrixhub.com
      </li>
    </ul>
  </div>
</body>
</html>
```